依頼詳細
弊社で取り扱う禁煙補助薬「ベルナミンパッチ」及び「ベルナミンガム」に関してA3のポスター及びA4チラシ(両面)をお願いいたします。
ポスター・チラシのイメージはポジティブなイメージにして欲しいです。
ポスターは特に禁煙メリットと方法がよく分かるインパクトが欲しいです。
チラシは表面は禁煙メリットと禁煙の方法としてのベルナミンがよく分かるようにして欲しいです。
裏面は、禁煙のコラムを文字中心で載せたいと思います。
全体を通してお願いしたいのは、危機感を絶対にあおらないイメージにしてください。
記載項目
ポスター:キャッチフレーズとして以下の3点と製品情報を入れてください。
「『禁煙』しないでタバコをやめる」・「禁煙支援薬剤師に相談」・「当店でベルナミン購入の方は「禁煙日記」と「すっきり道場」(24時間メール禁煙サポート:通常参加費10000円)が無料」(語尾などアレンジ可)
(ここで言う『禁煙』は辛い・苦しい・イライラ・我慢など、禁煙のネガティブなイメージをさしています)
製品情報:ベルナミンパッチstep1 14枚入り 5400円・1枚バラ売り 400円
ベルナミンパッチstep2 14枚入り 4800円・1枚バラ売り 380円
ベルナミン(ミント・フルーツ) 30個入り 2600円・1個バラ売り 100円

チラシ表面:上記に加え、禁煙してよかったこと。
(仕事や勉強に集中できるようになった・家族から信頼されるようになった・風邪を引きづらくなった・咳や痰が少なくなった・脱毛が減った・自らのタバコのにおいを気にしなくて良くなった・シミやしわが減り肌のつや・ハリが良くなった)

チラシ裏面:禁煙コラム(後述)
サイズ
ポスターはA3・チラシはA4両面
ページ数
両面
希望イメージ
シンプル 複雑
単色 カラフル
暗い 明るい
日常 高級
遊び心 厳粛
未来的 伝統的
女性的 男性的
希望する色
特にはないですが、とにかく明るい感じでお願いしたいです。
納品ファイル
• 高解像度JPG (.jpg)
• イラストレーター形式 (.ai)
補足説明
禁煙コラム1は以下の内容です。

タバコをやめると、こんな良い変化が・・・

1分禁煙すると・・・タバコのダメージから回復しようとする機能が働き始める。

20分で・・・血圧は正常近くまで下降する。脈拍も正常付近に復帰する。手の体温が聖女まで上昇する。

8時間で・・・血中の一酸化炭素レベルが正常域に戻り、血中酸素分圧が正常になって運動能力が改善する。

24時間で・・・心臓発作の確率が下がる。

48時間で・・・臭いと味の感覚が復活し始める。

48~72時間で・・・ニコチンが体から完全に抜ける。

72時間で・・・気管支の収縮がとれ、呼吸が楽になる。肺活量が増加し始める。

2週~3週間で・・・体の循環が改善する。歩行が楽になる。肺活量は30%回復する。

1~9ヶ月で・・・咳・静脈うっ血・全身倦怠・全身倦怠・呼吸促吐拍が改善する。

5年で・・・肺がんになる確率が半分に減る。

10年で・・・前がん状態の細胞が修復される。口腔がん・咽頭がん・食道がん・膀胱がん・胃がん・腎がん・すい臓がんになる確立が減少する。

しかし、上記のすべての利点は、たった一本のタバコで失われてしまう。
ベルナミンの製品ページはこちらです。
参考にしていただければ助かります。

http://www.velnamin.jp/patch/pa_products.html
禁煙コラム2つ目です。

禁煙に役立つ日常生活の工夫

吸いたくなったときには、次の方法から選んで試してみて、自分にあったやり方を見つけましょう。

・冷たい水や熱いお茶を飲む(ポイントは温度刺激と頻度。唇がしびれるほどの刺激が効果的)

・痛みや刺激で気を紛らわす(ボールペンなど、とがったものを利用して手のひらを押す。耳たぶを爪の先で押さえるのも有効。)

・歯ブラシを利用する(くわえる・噛む・軽く動かすなど・・・。食後すぐ、歯磨きで口をさっぱりさせるのも効果的。)

・宴会や煙の多い場所を避ける(禁煙をスタートした2週間は「逃げるが勝ち!」やむを得ず出席する場合は、吸う人の隣は絶対避けて、ノンアルコールの飲み物を用意しておこう。)

・野菜を食べる(イライラを抑え、便通を整える。細くきった料理用昆布は、口寂しさの解消にも。)

・絶えず体を動かす。深呼吸する(吸いたくなったら、とにかく動くこと。散歩・体操・入浴・掃除・歩く・ゆするでもOK!)

・その他・・・音楽・趣味に没頭する、マスクをする。寝る。コーヒーで吸いたくなる人は紅茶や日本茶に変える。あったかいミルクを飲む。禁煙日記をつける等
禁煙コラム1の「手の体温が聖女まで上昇する」→「手の体温が正常まで上昇する」にしてください。

以下は禁煙コラム3です。

mg数の少ないタバコのほうが害が多い?

→タバコをやめるためにまずmg数を落とそうと考えていませんか?
実は、mg数が少ないほうが体に有害ということをご存知でしょうか。
mg数の少ないタバコはニコチンの量こそ少ないですが、有害物質は同じだけ含まれています。
また、mg数の少ないタバコをすうときは、ニコチンの不足分を補おうと、深く吸い込んでしまう傾向にあります。
その為、有害物質が肺の奥まで行き渡ってしまうためタバコの害が大きいのです。
タバコのmg数で心筋梗塞などの発生率をみると、mg数の少ないタバコを吸っている人のほうが、mg数の多いタバコを吸っている人より高いというデータもあります。

電子タバコにも害がある?

→電子タバコの中には、ニコチンが少量含まれているものがあり、それがやめられなくなる人もいます。
また、水蒸気だけが常温で煙のように立ち上るということはありえません。
ということは、水蒸気以外のものも含まれているはずです。
含まれているものが有害かどうかは分かりませんが、いずれにせよ避けた方がよさそうです。

未成年(小・中・高校生)のほうがニコチン依存が強い?

→実は、未成年のほうが短い期間でニコチン依存ができてしまいます。
たった一本吸ってしまっただけでニコチン依存ができ、タバコがやめられなくなってしまう方も居ます。
ただ、未成年のニコチン依存は、お薬を使うと成人より少ない期間(早い人はパッチ1~3枚程度)で克服できる可能性があります。
お早めにご相談下さい。

タバコをやめると太る?
→禁煙した人のうち2/3の人に、食事量が増えなくても2kg程度の体重増加が認められます。
禁煙により胃腸への血流が回復して、消化吸収が改善されることからです。
また、タバコで麻痺していた味覚が回復して、食べ物が美味しく感じられることや、口寂しさから食事量が増えることもあります。
これは、体が正常に戻った証拠の2kgともいえます。
ただ、ニコチン切れのイライラから食事量が増え、2kg以上の体重増加するケースもあります。
これには、お薬を使うことでイライラを抑え、食事量を過度に増やさないようにしてくれますのでオススメです。
もう少し、いろいろな提案を見たいと思いましたので、締め切りを延ばしたいと思います。

弊社のポスターイメージは、morat様のご提案が近いです。
こういった分かりやすくて見やすい、そして色味の明るいものを希望しています。
http://www.quorvix.jp/work/proposal/2847315

チラシのイメージはtokunaga様のご提案が近いです。
禁煙のメリットが伝わりやすいと思います。
また、裏のコラムもきれいにまとまっていて分かりやすいと思いました。
http://www.quorvix.jp/work/proposal/2849022

多数のご提案、お待ちしておりますので、宜しくお願いいたします。

今回選んだ理由と致しましては、ポスターのインパクト、メッセージ性、チラシのまとめ方などを総合的に鑑みて、tokunaga様の作品が一番弊社のイメージに合うと思ったからです。
特に今回のコンセプト、「危機感をあおらない」ということを理解していただいて、誠実に作られたのだなということが一番伝わってきた作品でした。
以上の理由により、tokunaga様の作品を選ばせていただきました。

弊社のポスター・チラシ作成コンペに提案いただきました皆様、本当にありがとうございます。
素晴らしい提案が多く、選考に非常に迷いました。
このように沢山いろいろな感性を持った方々に、作品を提案いただけたのはうれしい限りです。
今回は残念ながらひとつの提案のみを採用させていただく形になりましたが、また、このような機会がありましたら、ご提案いただけたらと思います。
今回は、本当にありがとうございました。

```html
<!DOCTYPE html>
<html lang="ja">
<head>
<meta charset="utf-8">
<title>ベルナミン 禁煙サポートポスター</title>
<link href="https://fonts.googleapis.com/css2?family=M+PLUS+Rounded+1c:wght@500;700;800;900&display=swap" rel="stylesheet">
<style>
  :root {
    --red: #e8312f;
    --red-deep: #d2221f;
    --green: #2fa84a;
    --green-deep: #23923b;
    --ink: #333333;
    --paper: #ffffff;
    --pack-blue: #3f8fd0;
  }
  * { margin: 0; padding: 0; box-sizing: border-box; }
  html, body { width: 848px; height: 1200px; overflow: hidden; background: var(--paper); }
  body { font-family: "M PLUS Rounded 1c", sans-serif; color: var(--ink); }
  .poster { position: relative; width: 848px; height: 1200px; background: var(--paper); }

  .visual-panel { position: absolute; }
  .visual-panel--stress { left: 51px; top: 34px; width: 373px; height: 372px;
    background: linear-gradient(150deg, var(--red) 0%, var(--red-deep) 100%); }
  .visual-panel--relief { left: 424px; top: 410px; width: 382px; height: 382px;
    background: linear-gradient(150deg, var(--green) 0%, var(--green-deep) 100%); }

  .question { position: absolute; background: var(--paper); border-radius: 10px;
    display: flex; flex-direction: column; justify-content: center; align-items: center;
    font-weight: 900; line-height: 1.12; letter-spacing: -0.02em; }
  .question--stress { left: 432px; top: 40px; width: 370px; height: 358px;
    border: 6px solid var(--red); color: var(--red); font-size: 76px; }
  .question--relief { left: 46px; top: 416px; width: 370px; height: 372px;
    border: 6px solid var(--green); color: var(--green); font-size: 72px; }
  .question span { display: block; white-space: nowrap; }
  .question .bracketed { letter-spacing: -0.12em; margin-left: -0.3em; }

  .headline-band { position: absolute; left: 57px; top: 820px; width: 736px; height: 64px;
    background: var(--green); color: var(--paper); font-weight: 800; font-size: 42px;
    display: flex; align-items: center; justify-content: center; letter-spacing: 0.01em;
    white-space: nowrap; }

  .pharmacist-line { position: absolute; left: 57px; top: 896px; width: 736px; text-align: center;
    color: var(--green); font-weight: 800; font-size: 25.5px; letter-spacing: -0.02em;
    line-height: 1.3; white-space: nowrap; }

  .product-packs { position: absolute; left: 57px; top: 952px; width: 340px; height: 180px;
    background: linear-gradient(135deg, #e7f0f8 0%, var(--pack-blue) 55%, #2c6fb0 100%); }

  .offer-box { position: absolute; left: 412px; top: 952px; width: 380px; height: 112px;
    border: 3px solid var(--green); padding: 8px 6px; text-align: center;
    color: var(--red); font-weight: 800; line-height: 1.4;
    display: flex; flex-direction: column; justify-content: center; }
  .offer-box p { white-space: nowrap; }
  .offer-box .lead { font-size: 16px; }
  .offer-box .gift { font-size: 21px; letter-spacing: -0.02em; }
  .offer-box .note { font-size: 11.5px; letter-spacing: -0.02em; }

  .price-list { position: absolute; left: 412px; top: 1076px; width: 400px; list-style: none;
    font-size: 12.5px; font-weight: 700; line-height: 1.7; color: var(--ink); white-space: nowrap;
    letter-spacing: -0.01em; }
  .price-list small { font-size: 10px; }
</style>
</head>
<body>
<main class="poster">
  <div class="visual-panel visual-panel--stress" role="img" aria-label="タバコを指でへし折る白い手のイラスト"></div>
  <h2 class="question question--stress">
    <span>イライラ</span><span>我慢して</span><span>タバコを</span><span>やめる？</span>
  </h2>

  <h1 class="question question--relief">
    <span class="bracketed">『禁煙』を</span><span>しないで</span><span>タバコを</span><span>やめる？</span>
  </h1>
  <div class="visual-panel visual-panel--relief" role="img" aria-label="四つ葉のクローバーを持つ白い手のイラスト"></div>

  <p class="headline-band">「禁煙してよかった！」を皆様に!!</p>
  <p class="pharmacist-line">禁煙支援薬剤師があなたの禁煙のサポートをいたします。</p>

  <div class="product-packs" role="img" aria-label="ベルナミンパッチ step1・step2 の製品パッケージ写真"></div>

  <div class="offer-box">
    <p class="lead">当店でベルナミン購入の方は</p>
    <p class="gift">「禁煙日記」と「すっきり道場」</p>
    <p class="note">(24時間メール禁煙サポート:通常参加費10000円)が無料</p>
  </div>

  <ul class="price-list">
    <li>(ベルナミンパッチstep1) 14枚入り 5400円 <small>(1枚バラ売り 400円)</small></li>
    <li>(ベルナミンパッチstep2) 14枚入り 4800円 <small>(1枚バラ売り 380円)</small></li>
    <li>(ベルナミン(ミント・フルーツ)) 30個入り 2600円 <small>(1個バラ売り 100円)</small></li>
  </ul>
</main>
</body>
</html>
```